Virtual Reality medical education company

We are a new company that is offering virtual reality medical simulation suites. I have had a go at the initial web design www.brellowanstudio-example.com but as you can see I am no web designer!
I have the logo and some text which I'd like you to use - also some images. Any help with the SEO would be appreciated.

Target Market(s)

Students and faculty in medical and applied medical degrees

Industry/Entity Type

Education

Coding

Coded - Design and coding required

Number of Pages Required

5+ page

Font styles to use
Sans Serif

Requirements
Must have
• Home, Benefits, Simulation, Why Virtual, Modules, Contact Us
• Virtual reality scenes, either people using it or what they see.
• This is the patient we are using http://www.plexomarket-example.com/3d-models/rigged-hospital-patient-3d-max/4830291
Nice to have
• QRN Lumo or Pentara Drift headsets being worn
Should not have
• Non VR simulation, real patients/models, students looking at computer screens

```html
<!DOCTYPE html>
<html lang="en">
<head>
<meta charset="utf-8">
<title>Brellowan VR Coaching</title>
<link href="https://fonts.googleapis.com/css2?family=Raleway:wght@400;600;700;800&family=Open+Sans:wght@400;600;700&display=swap" rel="stylesheet">
<style>
:root{
  --blue:#0b72c6;
  --blue-dark:#1c48a6;
  --indigo:#2d3590;
  --sky:#e9f3fb;
  --ink:#222;
  --muted:#8a8f96;
  --line:#dfe6ee;
  --footer:#262626;
  --footer-deep:#161616;
  --white:#fff;
}
*{box-sizing:border-box;margin:0;padding:0}
html,body{width:1200px;height:3651px;overflow:hidden}
body{font-family:"Open Sans",sans-serif;color:var(--ink);background:var(--white);position:relative}
.abs{position:absolute}
h2.section-title{font-family:"Raleway",sans-serif;font-weight:800;font-size:19px;letter-spacing:3px;text-align:center;text-transform:uppercase}
.dots{text-align:center;font-size:12px;letter-spacing:4px;color:var(--blue);font-weight:700;margin-top:6px}
.btn{display:inline-flex;align-items:center;gap:10px;border:2px solid var(--blue);color:var(--blue);font:700 10px "Raleway",sans-serif;letter-spacing:1px;padding:0 14px;height:29px;background:var(--white)}
.btn.light{border-color:var(--white);color:var(--white);background:transparent}
.btn.light-fill{border-color:var(--white);background:var(--white);color:var(--blue)}
.topbar{top:0;left:0;width:1200px;height:36px;background:#f1f2f4}
.social{position:absolute;top:11px;display:flex;gap:12px;right:205px}
.social span{width:13px;height:13px;background:var(--blue-dark);display:block;border-radius:2px}
.header{top:36px;left:0;width:1200px;height:110px;background:var(--white)}
.brand{position:absolute;left:195px;top:34px;display:flex;align-items:center;gap:10px;font:800 20px "Raleway",sans-serif;color:var(--blue-dark);letter-spacing:.5px}
.brand i{width:30px;height:30px;border-radius:50%;background:var(--blue);display:block}
.info{position:absolute;top:32px;display:flex;gap:10px}
.info b{display:block;font:700 16px "Raleway",sans-serif}
.info small{font-size:11px;color:#444}
.nav{top:146px;left:0;width:1200px;height:51px;background:linear-gradient(90deg,var(--blue) 0%,var(--blue) 60%,var(--indigo) 100%)}
.nav ul{list-style:none;display:flex;gap:44px;position:absolute;left:195px;top:18px}
.nav li{font:700 12px "Raleway",sans-serif;color:var(--white);letter-spacing:1px}
.search{position:absolute;left:974px;top:0;width:50px;height:51px;background:#1e1e1e;display:flex;align-items:center;justify-content:center}
.hero{top:197px;left:0;width:1200px;height:903px;background:linear-gradient(180deg,#dfe6ec 0%,#eef2f5 50%,#f7f8fa 100%)}
.hero-photo{left:0;top:0;width:1200px;height:560px;background:linear-gradient(90deg,#d3dde5 0%,#eaeff3 45%,#dfe7ee 100%)}
.doctor{left:718px;top:46px;width:330px;height:512px;background:linear-gradient(180deg,#c9ad96 0%,#f3f4f6 35%,#e7eaee 100%);border-radius:120px 120px 0 0}
.hero-copy{left:175px;top:285px}
.hero-copy p{font:400 21px "Raleway",sans-serif;color:#333}
.hero-copy h1{font:800 21px "Raleway",sans-serif;color:var(--blue-dark);margin-top:2px}
.feature-col{top:690px;width:200px;color:var(--white)}
.feature-col h3{font:700 12px "Raleway",sans-serif;letter-spacing:.5px}
.feature-col h3:after{content:"";display:block;width:18px;height:2px;background:currentColor;margin:6px 0 10px}
.feature-col p{font-size:10.5px;line-height:16px}
.feature-col .btn{margin-top:20px}
.feature-col.on-light{color:var(--blue)}
.feature-col.on-light p{color:var(--blue)}
.welcome{top:1100px;left:0;width:1200px;height:348px;background:var(--white)}
.welcome .lead{position:absolute;left:180px;top:128px;width:840px;text-align:center;font-size:11px;line-height:18px;color:#9aa0a6}
.svc{position:absolute;top:210px;width:260px;display:flex;gap:14px}
.svc .ico{width:42px;height:42px;flex:none}
.svc h4{font:700 11px "Raleway",sans-serif;margin:6px 0 8px}
.svc p{font-size:10px;line-height:14px;color:#666}
.svc p em{color:var(--blue);font-style:normal}
.quick{top:1448px;left:0;width:1200px;height:346px;background:var(--blue)}
.quick h2{color:var(--white);margin-top:34px}
.field{position:absolute;border:1px solid #8fc0ea;color:#dbeaf7;font-size:10px;padding:6px 8px}
.benefits{top:1794px;left:0;width:1200px;height:506px;background:#f6f9fc}
.benefits .right-bg{left:600px;top:0;width:600px;height:506px;background:linear-gradient(90deg,#e3edf6,#eef4f9)}
.benefit{position:absolute;top:109px;width:440px;text-align:center}
.benefit .shot{width:224px;height:137px;margin:0 auto}
.benefit h3{font:600 15px "Raleway",sans-serif;color:var(--blue);margin:24px 0 10px}
.benefit p{font-size:10.5px;line-height:18px;color:#777}
.benefit .btn{margin-top:26px}
.simulation{top:2300px;left:0;width:1200px;height:353px;background:linear-gradient(180deg,#1275c6,#0b66b8)}
.simulation h2{color:var(--white);margin-top:40px}
.simulation .dots,.quick .dots{color:#bfe0fa}
.simulation p{position:absolute;left:258px;top:92px;width:684px;text-align:center;color:var(--white);font-size:11.5px;line-height:19px}
.why{top:2653px;left:0;width:1200px;height:275px;background:#f4f6f9}
.why h2{margin-top:42px}
.why-item{position:absolute;top:135px;display:flex;align-items:center;gap:14px;font:400 16px "Raleway",sans-serif;color:#333}
.modules{top:2928px;left:0;width:1200px;height:321px;background:var(--white)}
.modules-img{left:0;top:0;width:458px;height:321px;background:linear-gradient(135deg,#4f86b8,#2a5f95 60%,#5b8fc0)}
.modules-img span{position:absolute;left:118px;top:140px;font:800 28px "Raleway",sans-serif;color:var(--white);letter-spacing:3px}
.mod{position:absolute;width:247px;height:160px;border-right:1px solid var(--line);border-bottom:1px solid var(--line);text-align:center;padding-top:36px}
.mod h5{font:700 10px "Raleway",sans-serif;letter-spacing:.5px;margin:8px 0 6px}
.mod p{font-size:9.5px;line-height:13px;color:#777;padding:0 40px}
.infobar{top:3249px;left:0;width:1200px;height:91px;background:var(--blue);color:var(--white)}
.ib{position:absolute;top:22px;display:flex;gap:22px}
.ib .box{width:44px;height:44px;background:rgba(255,255,255,.18);display:flex;align-items:center;justify-content:center}
.ib b{font:700 11px "Raleway",sans-serif;display:block;margin-bottom:6px}
.ib small{font-size:10px}
.footer{top:3340px;left:0;width:1200px;height:262px;background:var(--footer);color:#bbb}
.footer .brand{left:185px;top:40px;color:var(--white);font-size:17px}
.footer .about{position:absolute;left:185px;top:120px;width:200px;font-size:9.5px;line-height:14px}
.footer .fsocial{position:absolute;left:185px;top:213px;display:flex;gap:10px}
.footer .fsocial span{width:22px;height:22px;border:1px solid #999}
.footer h6{position:absolute;font:700 12px "Raleway",sans-serif;color:var(--white);top:64px}
.links{position:absolute;top:110px;list-style:none;font-size:10px;line-height:32px}
.links li:before{content:"› ";color:#888}
.news p{position:absolute;left:772px;top:110px;font-size:11px}
.news .email{position:absolute;left:772px;top:136px;width:214px;height:36px;border:1px solid #444;font-size:10px;padding:11px 10px;color:#888}
.news .sub{position:absolute;left:986px;top:136px;width:54px;height:36px;background:var(--blue);color:var(--white);font:700 10px "Raleway",sans-serif;display:flex;align-items:center;justify-content:center}
.bottom{top:3602px;left:0;width:1200px;height:49px;background:var(--footer-deep);color:#ccc;font-size:10px}
.bottom span{position:absolute;left:185px;top:18px}
.totop{position:absolute;left:986px;top:28px;width:30px;height:21px;background:var(--blue);display:flex;align-items:center;justify-content:center}
</style>
</head>
<body>

<div class="abs topbar"><div class="social"><span></span><span></span><span></span><span></span></div></div>

<header class="abs header">
  <div class="brand"><i></i>Brellowan VR Coaching</div>
  <div class="info" style="left:620px">
    <svg width="22" height="28" viewBox="0 0 22 28"><path d="M11 1C5.5 1 1 5.4 1 10.8 1 18 11 27 11 27s10-9 10-16.2C21 5.4 16.5 1 11 1z" fill="#0b72c6"/><circle cx="11" cy="11" r="3.5" fill="#fff"/></svg>
    <div><b>OUR LOCATION</b><small>320,Duis aute irure dolor voluptat</small></div>
  </div>
  <div class="info" style="left:838px">
    <svg width="24" height="24" viewBox="0 0 24 24"><path d="M6 2l4 5-2 3c1.5 3 3 4.5 6 6l3-2 5 4-3 4C10 21 3 14 2 5z" fill="#0b72c6"/></svg>
    <div><b>(+1)800 555 0143</b><small>Call Us Now</small></div>
  </div>
</header>

<nav class="abs nav">
  <ul><li>HOME</li><li>BENEFITS</li><li>SIMULATION</li><li>WHY VIRTUAL</li><li>MODULES</li><li>CONTACT US</li></ul>
  <div class="search"><svg width="18" height="18" viewBox="0 0 18 18"><circle cx="7.5" cy="7.5" r="5.5" stroke="#fff" stroke-width="2.2" fill="none"/><path d="M12 12l5 5" stroke="#fff" stroke-width="2.4"/></svg></div>
</nav>

<section class="abs hero">
  <div class="abs hero-photo" role="img" aria-label="Blurred hospital corridor background"></div>
  <div class="abs doctor" role="img" aria-label="Doctor in white coat with stethoscope, arms folded"></div>
  <div class="abs hero-copy">
    <p>Cost Effective, Real-time VR Environment&nbsp; For</p>
    <h1>Undergraduate Medical Imaging Students</h1>
  </div>
  <svg class="abs" style="left:0;top:0" width="1200" height="903" viewBox="0 0 1200 903">
    <polygon points="0,414 600,533 1200,414 1200,430 600,545 0,430" fill="#8fc3ec"/>
    <polygon points="0,430 600,545 600,903 0,903" fill="#0b6fc4"/>
    <polygon points="0,430 600,545 600,575 0,470" fill="#1c48a6"/>
    <polygon points="600,545 1200,430 1200,903 600,903" fill="#f7f9fb"/>
  </svg>
  <div class="abs feature-col" style="left:175px"><h3>OUR EXPERTS</h3><p>Quis autem vel eum iure repreben qui in ea voluptate velit esse quam nihil molestiae consequaturqui</p><span class="btn light-fill">READ MORE ›</span></div>
  <div class="abs feature-col" style="left:402px"><h3>OUR TRAINING</h3><p>Quis autem vel eum iure repreben qui in ea voluptate velit esse quam nihil molestiae consequaturqui</p><span class="btn light-fill">READ MORE ›</span></div>
  <div class="abs feature-col on-light" style="left:626px"><h3>OUR FACILITIES</h3><p>Temporibus autem quibusdam aut officiis debitis aut rerum necessitatibus saepe eveniet</p><span class="btn">READ MORE ›</span></div>
  <div class="abs feature-col on-light" style="left:852px"><h3>OUR RESEARCH</h3><p>Quis autem vel eum iure repreben qui in ea voluptate velit esse quam nihil molestiae consequaturqui</p><span class="btn">READ MORE ›</span></div>
</section>

<section class="abs welcome">
  <h2 class="section-title" style="margin-top:50px">Welcome to Brellowan</h2>
  <div class="dots">+++</div>
  <p class="lead">The element of interaction is of utmost importance to make the user really feel free to get involved with the virtual environment. According to Pellington Review magazine the virtual reality (VR) market is expected to grow to US$407.51 million and reach more than 25 million users by 2018.</p>
  <div class="svc" style="left:180px">
    <svg class="ico" viewBox="0 0 42 42"><circle cx="21" cy="21" r="18" fill="none" stroke="#0b72c6" stroke-width="2"/><circle cx="21" cy="12" r="3" fill="#0b72c6"/><path d="M21 16v10h7M17 22a6 6 0 1 0 7 8" stroke="#0b72c6" stroke-width="2" fill="none"/></svg>
    <div><h4>THE PATIENT</h4><p>Brellowan VR Coaching has created different patients to reflect the different sizes and genders that students will be working within the clinical environment<em>[...]</em></p></div>
  </div>
  <div class="svc" style="left:472px">
    <svg class="ico" viewBox="0 0 42 42"><circle cx="21" cy="21" r="18" fill="#e6f1fb"/><path d="M13 26a9 9 0 0 1 16 0" stroke="#0b72c6" stroke-width="3" fill="none"/><circle cx="21" cy="25" r="3" fill="#0b72c6"/></svg>
    <div><h4>EQUIPMENT</h4><p>Brellowan VR Coaching offers the latest computed radiography (CR) and direct digital radiography (DDR) equipment<em>[...]</em></p></div>
  </div>
  <div class="svc" style="left:764px">
    <svg class="ico" viewBox="0 0 42 42"><path d="M6 28l12-8 4 4-12 8z" fill="#0b72c6"/><path d="M22 18l14-8M24 22l14 0M22 26l14 8" stroke="#0b72c6" stroke-width="2"/></svg>
    <div><h4>EXPOSURE SETTING AND IMAGING</h4><p>Just like the clinical environment, imaging is conducted from behind a lead glass window which the student has to walk behind to access the console unit<em>[...]</em></p></div>
  </div>
</section>

<section class="abs quick">
  <h2 class="section-title">Quick Contact Form</h2>
  <div class="dots">+++</div>
  <div class="field" style="left:195px;top:95px;width:418px;height:27px">Your Name..</div>
  <div class="field" style="left:626px;top:95px;width:391px;height:27px">Subject</div>
  <div class="field" style="left:195px;top:139px;width:822px;height:27px">Email Address</div>
  <div class="field" style="left:195px;top:183px;width:822px;height:85px">Message..</div>
  <span class="btn light-fill abs" style="left:942px;top:290px;width:75px;justify-content:center">SUBMIT</span>
</section>

<section class="abs benefits">
  <div class="abs right-bg" role="img" aria-label="Faded photo of a doctor"></div>
  <h2 class="section-title abs" style="top:39px;width:1200px">Our Benefits</h2>
  <div class="dots abs" style="top:68px;width:1200px">+++</div>
  <div class="benefit" style="left:160px">
    <div class="shot" role="img" aria-label="Dark X-ray image of a spine" style="background:linear-gradient(180deg,#111,#3a3a3a 50%,#0d0d0d)"></div>
    <h3>Benefits For Students</h3>
    <p>Students require hands on learning which encourages them to actively think about information, make choices, and execute learning skills for defined physical tasks. Simulators have been used in the military and aeronautical industry for years and have been shown to dramatically increase both the cognitive and motor accuracy of the participants...</p>
    <span class="btn">READ MORE ›</span>
  </div>
  <div class="benefit" style="left:600px">
    <div class="shot" role="img" aria-label="Student using VR headset at imaging console" style="background:linear-gradient(135deg,#8e8a84,#c9c6c0 50%,#4a4d55)"></div>
    <h3>Benefits For Training Institutes</h3>
    <p>For training institutes, having live radiation equipment means building special rooms for them to be housed in, with strengthened ceilings and radiation protected walls and floors. The opportunity cost of having a room or two used for these machines is high – what else could be done with the space during the times when the radiation units are not in use...</p>
    <span class="btn">READ MORE ›</span>
  </div>
</section>

<section class="abs simulation">
  <h2 class="section-title">Simulation</h2>
  <div class="dots">+++</div>
  <p>Unfavourable comparisons have been made between medicine and other high-risk industries. The risk of dying in an air crash is one in 10 million. When a person is admitted to hospital, their risk of dying or being seriously harmed by medical error is one in 300. It is too long a bow to draw to suggest that this is, in part, because using simulation to constantly practise skills and rehearse emergency situations is a vital part of air safety?<br>Studies of simulation training for surgical skills have shown that surgeons trained using simulation techniques make fewer errors and carry out technically more exact procedures. Simulation offers an important route to safer care for patients and needs to be more fully integrated into the health service</p>
  <span class="btn light abs" style="left:552px;top:287px">READ MORE ›</span>
</section>

<section class="abs why">
  <h2 class="section-title">Why Virtual</h2>
  <div class="dots">+++</div>
  <div class="why-item" style="left:238px"><svg width="38" height="30" viewBox="0 0 38 30"><path d="M2 28h34M6 26V18h5v8M15 26V13h5v13M24 26V9h5v17M4 14l10-8 8 4 12-8" stroke="#0b72c6" stroke-width="1.8" fill="none"/></svg>Growing Market</div>
  <div class="why-item" style="left:480px"><svg width="44" height="40" viewBox="0 0 44 40"><circle cx="20" cy="18" r="14" stroke="#0b72c6" stroke-width="1.8" fill="none"/><rect x="8" y="14" width="24" height="10" rx="3" fill="#0b72c6"/><path d="M36 10a10 10 0 0 1 0 16" stroke="#0b72c6" stroke-width="1.8" fill="none"/></svg>Real Time VR Environment</div>
  <div class="why-item" style="left:792px"><svg width="38" height="44" viewBox="0 0 38 44"><circle cx="19" cy="7" r="5" stroke="#0b72c6" stroke-width="1.8" fill="none"/><path d="M10 18h18v14H10zM4 22h8M26 22h8M14 32v10M24 32v10" stroke="#0b72c6" stroke-width="1.8" fill="none"/></svg>Hands on Experience</div>
  <span class="btn abs" style="left:552px;top:207px">READ MORE ›</span>
</section>

<section class="abs modules">
  <div class="abs modules-img" role="img" aria-label="Virtual radiography room with patient lying on imaging table"><span>OUR MODULES</span></div>
  <div class="mod" style="left:458px;top:0"><svg width="26" height="24" viewBox="0 0 26 24"><rect x="3" y="4" width="20" height="16" stroke="#0b72c6" stroke-width="1.8" fill="none"/><path d="M13 4v16M3 12h20" stroke="#0b72c6" stroke-width="1.5"/></svg><h5>RADIOGRAPHY SUITE</h5><p>Itaque earum rerum hic tenetur a sapiente delectus</p></div>
  <div class="mod" style="left:705px;top:0"><svg width="26" height="24" viewBox="0 0 26 24"><path d="M13 2v9M13 8c-3 0-9 2-9 10 0 3 3 4 6 2l3-5 3 5c3 2 6 1 6-2 0-8-6-10-9-10" stroke="#0b72c6" stroke-width="1.8" fill="none"/></svg><h5>ANATOMY MODULE</h5><p>Reiciendis voluptatibus maiores alias consequatur doloribus</p></div>
  <div class="mod" style="left:952px;top:0;border-right:none"><svg width="26" height="24" viewBox="0 0 26 24"><circle cx="13" cy="12" r="10" stroke="#0b72c6" stroke-width="1.8" fill="none"/><circle cx="13" cy="12" r="4" stroke="#0b72c6" stroke-width="1.8" fill="none"/></svg><h5>MRI MODULE</h5><p>Nobis est eligendi optio cumque nihil impedit quo minus</p></div>
  <div class="mod" style="left:458px;top:160px"><svg width="26" height="24" viewBox="0 0 26 24"><circle cx="13" cy="12" r="10" stroke="#0b72c6" stroke-width="1.8" fill="none"/><path d="M8 14h10" stroke="#0b72c6" stroke-width="3"/></svg><h5>CT MODULE</h5><p>Tempora incidunt ut labore et dolore magnam aliquam</p></div>
  <div class="mod" style="left:705px;top:160px"><svg width="26" height="24" viewBox="0 0 26 24"><circle cx="7" cy="18" r="3" stroke="#0b72c6" stroke-width="1.8" fill="none"/><circle cx="19" cy="18" r="3" stroke="#0b72c6" stroke-width="1.8" fill="none"/><path d="M9 16L20 3M17 16L6 3" stroke="#0b72c6" stroke-width="1.8"/></svg><h5>THEATRE MODULE</h5><p>Consequuntur magni dolores eos qui ratione voluptatem</p></div>
  <div class="mod" style="left:952px;top:160px;border-right:none"><svg width="26" height="24" viewBox="0 0 26 24"><rect x="7" y="1" width="12" height="22" rx="2" stroke="#0b72c6" stroke-width="1.8" fill="none"/><circle cx="13" cy="19" r="1.2" fill="#0b72c6"/></svg><h5>MOBILE SUITES</h5><p>Et harum quidem rerum facilis est et expedita distinctio</p></div>
</section>

<section class="abs infobar">
  <div class="ib" style="left:160px"><div class="box"><svg width="16" height="20" viewBox="0 0 22 28"><path d="M11 1C5.5 1 1 5.4 1 10.8 1 18 11 27 11 27s10-9 10-16.2C21 5.4 16.5 1 11 1z" fill="none" stroke="#fff" stroke-width="2"/><circle cx="11" cy="11" r="3" fill="#fff"/></svg></div><div><b>OUR ADDRESS</b><small>320,Duis aute irure dolor<br>voluptat</small></div></div>
  <div class="ib" style="left:452px"><div class="box"><svg width="20" height="20" viewBox="0 0 24 24"><path d="M6 2l4 5-2 3c1.5 3 3 4.5 6 6l3-2 5 4-3 4C10 21 3 14 2 5z" fill="none" stroke="#fff" stroke-width="1.8"/></svg></div><div><b>CONTACT NUMBER</b><small>(+1)800 555 0143</small></div></div>
  <div class="ib" style="left:745px"><div class="box"><svg width="22" height="16" viewBox="0 0 22 16"><rect x="1" y="1" width="20" height="14" fill="none" stroke="#fff" stroke-width="1.6"/><path d="M1 1l10 8 10-8" fill="none" stroke="#fff" stroke-width="1.6"/></svg></div><div><b>OUR EMAIL</b><small>j.marlow@brellowanstudio-example.com</small></div></div>
</section>

<footer class="abs footer">
  <div class="brand">Brellowan VR Coaching</div>
  <p class="about">Virtual learning through a VR system could open up a new window of opportunity for STEM education. Difficult and often mundane content to be presented in a new and exciting way.</p>
  <div class="fsocial"><span></span><span></span><span></span><span></span></div>
  <h6 style="left:472px">OUR LINKS</h6>
  <ul class="links" style="left:485px"><li>Home</li><li>Benefits</li><li>Simulation</li></ul>
  <ul class="links" style="left:590px"><li>Why Virtual</li><li>Our Modules</li><li>Contact Us</li></ul>
  <h6 style="left:772px">NEWSLETTER</h6>
  <div class="news"><p>Subscribe to our newsletter for latest updates</p><div class="email">Email Address</div><div class="sub">SUBMIT</div></div>
</footer>

<div class="abs bottom"><span>©copyright information here</span><div class="totop"><svg width="10" height="7" viewBox="0 0 10 7"><path d="M1 6l4-4 4 4" stroke="#fff" stroke-width="1.8" fill="none"/></svg></div></div>

</body>
</html>
```